Plastic Seasoning Bottle Design Label

I am looking to get a label design that's going on plastic seasoning bottles. My company which deals with seasons/spices. My company sells healthy all natural seasons so I would like the label to have a design of natural. I also would like a hot pepper on there showing it's hot and also other red indentations like red fire or something that shows it's very hot !!!
The company name is Brisk Meadow Harvest which I would like in light green letters.
There are six different seasonings favors which are:
Barbecue
Garlic
Lemon
Chili
Poultry/Meat
Seafood

The label size: 190.00mm x 111.00mm

Thanks

I would like for the colors to be:
Green
Light Green
Red ( For Hot )
White
Seafood
All of them will be hot as it will show on the label.

Hello, Please include on the labels pictures of the foods associated with the seasoning. Example: Seafood= Fish,lobster,clams,shrimp,scallops,eel,octopus,squid and muscles which will show that it's also very hot. As for seasonings like the Lemon you could just put pictures of lemons which are showing also that there hot as all of the seasoning are hot also. Garlic would be the same as the lemon with just picture also showing it's very hot. Meat would show different kinds of beef such as steak,hamburgers. Also chicken and ham which will show that it's also very hot. Barbecue and Chili you can feel free to show different ideas on that as they will also show that they are very hot as all of them are. The label size is 190.00mm x 111.00mm If you need more time to work on this project please feel free to let me know as I have no problem extending the dead line. Thanks

Hello, In the last update I mentioned Ham as I met to put Ribs not Ham. Thanks

Hello, The budget has been increased. It's now 201.00

Hello, At the end of the company name I would like to have a small TM at the end of the company name as the the has a trade mark on it. Thanks

Industry/Entity Type

Plastic

Font styles to use
Serif
Sans Serif
Decorative
Script
Other font styles liked:
• Georgia,Italic,Bold

```html
<!DOCTYPE html>
<html lang="en">
<head>
<meta charset="utf-8">
<title>Brisk Meadow Harvest – Seasoning Label</title>
<link rel="stylesheet" href="https://fonts.googleapis.com/css2?family=Francois+One&family=Oswald:wght@600&family=Arimo:wght@400;700&display=swap">
<style>
  :root {
    --meadow-deep: #3f9a1c;
    --meadow-mid: #6cc52a;
    --meadow-light: #b6ec6a;
    --leaf-text: #2e7d12;
    --title-green: #c8f7a0;
    --hot-red: #d4120e;
    --hot-orange: #ef5a10;
    --hot-yellow: #f3d21a;
    --header-yellow: #f6ea1c;
    --frame-red: #8e0f0c;
    --white: #ffffff;
  }
  html, body {
    margin: 0;
    padding: 0;
    overflow: hidden;
  }
  body {
    width: 1200px;
    height: 701px;
  }
  .label {
    position: relative;
    width: 1200px;
    height: 701px;
    overflow: hidden;
    background: radial-gradient(ellipse at 55% 45%, var(--meadow-light) 0%, var(--meadow-mid) 45%, var(--meadow-deep) 100%);
    font-family: "Arimo", Arial, sans-serif;
  }
  .brand-name {
    position: absolute;
    top: 30px;
    left: 0;
    width: 1200px;
    margin: 0;
    text-align: center;
    font-family: "Francois One", "Arial Narrow", sans-serif;
    font-weight: 400;
    font-size: 44px;
    letter-spacing: 2px;
    color: var(--title-green);
    text-transform: uppercase;
  }
  .brand-name sup {
    font-size: 17px;
    letter-spacing: 0;
  }

  .flavor-tile {
    position: absolute;
    width: 203px;
    height: 165px;
    box-sizing: border-box;
    border: 4px solid var(--frame-red);
    background: linear-gradient(to bottom, var(--hot-yellow) 0%, var(--hot-orange) 45%, var(--hot-red) 100%);
    box-shadow: 2px 3px 6px rgba(0,0,0,0.35);
  }
  .flavor-tile--garlic { left: 67px; top: 107px; }
  .flavor-tile--lemon { left: 312px; top: 107px; }
  .flavor-tile--chili { left: 67px; top: 329px; }
  .flavor-tile--barbecue { left: 312px; top: 329px; }
  .flavor-tile__photo {
    position: absolute;
    left: 55px;
    top: 6px;
    width: 130px;
    height: 96px;
  }
  .flavor-tile--garlic .flavor-tile__photo { background: radial-gradient(ellipse, #fbf7ee 30%, rgba(221,210,192,0.7) 65%, transparent 72%); }
  .flavor-tile--lemon .flavor-tile__photo { background: radial-gradient(ellipse, #fff27a 30%, rgba(242,204,24,0.8) 62%, transparent 72%); }
  .flavor-tile--chili .flavor-tile__photo { background: radial-gradient(ellipse, #b8120a 25%, rgba(158,11,8,0.6) 55%, transparent 70%); }
  .flavor-tile--barbecue .flavor-tile__photo { background: radial-gradient(ellipse, #c97a4a 30%, rgba(140,68,32,0.7) 62%, transparent 72%); }
  .heat-mark {
    position: absolute;
    background: radial-gradient(ellipse at 50% 70%, rgba(246,220,40,0.9) 0%, rgba(239,90,16,0.6) 45%, transparent 72%);
  }
  .flavor-tile .heat-mark {
    left: -4px;
    bottom: -2px;
    width: 72px;
    height: 100px;
  }
  .flavor-tile__name {
    position: absolute;
    right: 18px;
    bottom: 10px;
    font-family: "Arimo", Arial, sans-serif;
    font-size: 36px;
    line-height: 1;
    color: var(--white);
    text-shadow: 1px 1px 2px rgba(0,0,0,0.5);
  }
  .flavor-tile--lemon .flavor-tile__name { font-size: 38px; right: 12px; }
  .flavor-tile--barbecue .flavor-tile__name { font-size: 28px; right: 10px; bottom: 14px; }

  .spice-spill {
    position: absolute;
    left: 78px;
    top: 523px;
    width: 424px;
    height: 145px;
    border-radius: 30px 30px 50% 50%;
    background: linear-gradient(90deg, #b5261b 0%, #8b3a22 15%, #a88a6a 30%, #c6a98a 45%, #d98d20 60%, #e2b735 75%, #e8d4a2 100%);
    opacity: 0.9;
  }

  .food-panel {
    position: absolute;
    box-sizing: border-box;
    border: 4px solid var(--frame-red);
    background: linear-gradient(to bottom, var(--hot-yellow) 0%, var(--hot-orange) 40%, var(--hot-red) 100%);
    box-shadow: 2px 3px 6px rgba(0,0,0,0.35);
    text-align: center;
  }
  .food-panel--seafood { left: 590px; top: 107px; width: 194px; height: 561px; }
  .food-panel--poultry { left: 841px; top: 107px; width: 317px; height: 338px; }
  .food-panel__title {
    margin: 0;
    font-family: "Oswald", "Arial Narrow", sans-serif;
    font-weight: 600;
    font-size: 36px;
    line-height: 1;
    color: var(--leaf-text);
    background: var(--header-yellow);
  }
  .food-panel--seafood .food-panel__title { margin: 8px 10px 0; padding: 4px 0 6px; }
  .food-panel--poultry .food-panel__title { margin: 14px 14px 0; padding: 6px 0 8px; font-size: 33px; }
  .food-panel__list {
    list-style: none;
    margin: 0;
    padding: 0;
    color: var(--leaf-text);
    font-family: "Arimo", Arial, sans-serif;
  }
  .food-panel--seafood .food-panel__list { margin-top: 6px; font-size: 35px; line-height: 37.5px; }
  .food-panel--poultry .food-panel__list { margin-top: 52px; font-size: 35px; line-height: 42px; }
  .food-panel .heat-mark {
    left: -6px;
    bottom: -4px;
    width: 80px;
    height: 110px;
  }
</style>
</head>
<body>
<main class="label">
  <h1 class="brand-name">Brisk Meadow Harvest<sup>™</sup></h1>

  <section class="flavor-tile flavor-tile--garlic">
    <div class="flavor-tile__photo" role="img" aria-label="Garlic bulb and cloves"></div>
    <div class="heat-mark" role="img" aria-label="Flame illustration"></div>
    <span class="flavor-tile__name">Garlic</span>
  </section>
  <section class="flavor-tile flavor-tile--lemon">
    <div class="flavor-tile__photo" role="img" aria-label="Whole lemon and lemon slice"></div>
    <div class="heat-mark" role="img" aria-label="Flame illustration"></div>
    <span class="flavor-tile__name">Lemon</span>
  </section>
  <section class="flavor-tile flavor-tile--chili">
    <div class="flavor-tile__photo" role="img" aria-label="Red chili pepper"></div>
    <div class="heat-mark" role="img" aria-label="Flame illustration"></div>
    <span class="flavor-tile__name">Chili</span>
  </section>
  <section class="flavor-tile flavor-tile--barbecue">
    <div class="flavor-tile__photo" role="img" aria-label="Grilled barbecue steak"></div>
    <div class="heat-mark" role="img" aria-label="Flame illustration"></div>
    <span class="flavor-tile__name">Barbecue</span>
  </section>

  <div class="spice-spill" role="img" aria-label="Row of tipped spice jars spilling colourful ground spices"></div>

  <section class="food-panel food-panel--seafood">
    <h2 class="food-panel__title">SEAFOOD</h2>
    <ul class="food-panel__list">
      <li>Fish</li>
      <li>Lobster</li>
      <li>Clams,</li>
      <li>Shrimp</li>
      <li>Scallops</li>
      <li>Eel</li>
      <li>Octopus</li>
      <li>Squid</li>
      <li>Mussel</li>
    </ul>
    <div class="heat-mark" role="img" aria-label="Flame illustration"></div>
  </section>

  <section class="food-panel food-panel--poultry">
    <h2 class="food-panel__title">POULTRY/MEAT</h2>
    <ul class="food-panel__list">
      <li>Steak</li>
      <li>Hamburgers</li>
      <li>Chicken</li>
      <li>Ribs</li>
    </ul>
    <div class="heat-mark" role="img" aria-label="Flame illustration"></div>
  </section>
</main>
</body>
</html>
```